Artificial Intelligence based service Veltranoquest.ai

Looking for a website for service designed for driving schools to deliver AI based solutions and features. File are to include various pages from contact to list of services to faqs, demos and more. we are looking for a website for AI based service for driving schools. services will include things like chat bots, voice agent, document processing and ai based marketing.

Target Market(s)

driving school owners and managers.

Industry/Entity Type

software and AI

Number of Pages Required

4 page

Font styles to use
Sans Serif

Requirements
Must have
• clean and easy to navigate pages. responsive. also delivery via FIGMA.

```html
<!DOCTYPE html>
<html lang="en">
<head>
<meta charset="UTF-8">
<title>Veltranoquest.ai – 24/7 Voice Agent for Driving Schools</title>
<link href="https://fonts.googleapis.com/css2?family=Poppins:wght@400;500;600;700&family=Lexend:wght@500&display=swap" rel="stylesheet">
<style>
:root{
  --bg-top:#0b1d44;
  --bg-mid:#061433;
  --bg-deep:#030b1f;
  --green:#7cc36d;
  --white:#ffffff;
  --muted:#d7def0;
  --card:#0e2452;
  --card-edge:#2b5bc2;
  --panel:#13295c;
  --line:#24365e;
}
*{margin:0;padding:0;box-sizing:border-box}
html,body{width:1200px;height:3516px;overflow:hidden}
body{
  position:relative;
  font-family:'Poppins',sans-serif;
  color:var(--white);
  background:linear-gradient(180deg,var(--bg-top) 0%,var(--bg-mid) 20%,var(--bg-deep) 55%,var(--bg-mid) 80%,var(--bg-top) 100%);
}
.abs{position:absolute}
.accent{color:var(--green);font-weight:500}
.brand{font-family:'Poppins',sans-serif;font-weight:600;color:var(--white);display:flex;align-items:center;gap:10px;white-space:nowrap}
.brand-dot{width:12px;height:12px;border-radius:50%;background:var(--green)}
.btn{position:absolute;display:flex;align-items:center;justify-content:center;border-radius:30px;font-size:15px;font-weight:400;white-space:nowrap}
.btn-green{background:var(--green);color:var(--white)}
.btn-outline{border:1.5px solid var(--white);color:var(--white)}
.btn-light{background:var(--white);color:#1c2b4e}
.section-title{position:absolute;left:0;width:1200px;text-align:center;font-size:36px;font-weight:600;letter-spacing:.3px}
.photo{position:absolute;border-radius:6px}
/* hero */
.hero-title{left:86px;top:180px;font-size:53px;font-weight:700;line-height:63px;letter-spacing:.5px}
.hero-sub{left:88px;top:307px;font-family:'Lexend',sans-serif;font-size:38px;font-weight:500}
.hero-tag{left:89px;top:366px;width:520px;font-size:13.5px;color:var(--muted);white-space:nowrap}
/* voice band placeholder */
.voice-band{position:absolute;left:0;width:1200px;height:240px;background:radial-gradient(ellipse 30% 50% at var(--cx) 50%,rgba(124,195,109,.35),rgba(124,195,109,0) 70%),linear-gradient(180deg,transparent 44%,rgba(124,195,109,.28) 46%,rgba(124,195,109,.28) 54%,transparent 56%)}
/* why */
.why-title{left:650px;top:876px;font-size:36px;font-weight:600;line-height:41px}
.why-text{left:652px;top:970px;width:460px;font-size:14.5px;line-height:20px;color:var(--muted)}
/* problems */
.problem{position:absolute;top:1340px;width:309px;height:283px;border:1.5px solid var(--card-edge);border-radius:6px;background:linear-gradient(180deg,var(--card),#0a1b40);padding:22px 17px}
.problem svg{width:44px;height:44px;display:block;margin-bottom:12px}
.problem h3{font-size:15px;font-weight:600;line-height:18px;margin-bottom:6px}
.problem p,.problem li{font-size:12.5px;line-height:19px;color:var(--muted)}
.problem ul{list-style:none;display:flex;flex-wrap:wrap;column-gap:14px;margin:6px 0 6px}
.problem li::before{content:"";display:inline-block;width:5px;height:5px;border-radius:50%;background:var(--green);margin-right:5px;vertical-align:middle}
.problem .result{margin-top:10px}
.problem b{color:var(--green);font-weight:500}
.dots{left:586px;top:1647px;display:flex;gap:9px}
.dots span{width:9px;height:9px;border-radius:50%;background:var(--white)}
.dots span:first-child{background:var(--green)}
/* benefits */
.orbit{left:418px;top:2045px;width:366px;height:366px;border-radius:50%;border:1.5px solid var(--line)}
.benefit-icon{position:absolute;width:52px;height:52px;border-radius:50%;background:var(--green);display:flex;align-items:center;justify-content:center;box-shadow:0 0 0 4px rgba(124,195,109,.18)}
.benefit-icon svg{width:28px;height:28px}
.benefit{position:absolute;font-size:15px;font-weight:600;line-height:18px;text-transform:uppercase;white-space:nowrap}
.benefit.left{text-align:right}
.center-brand{left:460px;top:2205px;width:282px;justify-content:center;font-size:30px}
/* testimonials */
.quote{position:absolute;top:2577px;width:218px;height:248px;border:1px solid #1f3a72;border-radius:6px;background:linear-gradient(180deg,#0b1e48,#07163a);padding:14px 16px 18px;display:flex;flex-direction:column}
.quote-mark{font-family:Georgia,serif;font-size:70px;line-height:50px;color:var(--green);font-weight:700;height:40px}
.quote p{font-size:11px;line-height:20px;color:var(--muted);margin-top:8px}
.quote .author{display:flex;align-items:center;gap:8px;margin-top:auto;font-size:13px;font-weight:500}
.quote .author::before{content:"";width:28px;height:1.5px;background:var(--white)}
/* cta */
.cta{left:90px;top:2932px;width:1020px;height:300px;border:1.5px solid var(--card-edge);border-radius:6px;background:linear-gradient(120deg,#0a2150,#143a7a 60%,#0c2557)}
.cta-art{left:27px;top:2965px;width:370px;height:230px;border-radius:40% 10% 40% 20%;background:radial-gradient(ellipse at 45% 50%,rgba(80,190,230,.45),rgba(30,90,160,.2) 60%,transparent 75%)}
.cta-title{left:533px;top:2981px;font-size:36px;font-weight:600;line-height:42px}
.cta-text{left:534px;top:3068px;font-size:15px;color:var(--muted)}
/* footer */
.footer-brand{left:111px;top:3280px;font-size:34px}
.social{position:absolute;top:3290px;width:35px;height:35px;border-radius:50%;background:#1a2c52}
.social.on{background:var(--green)}
.footer-rule{left:111px;top:3371px;width:960px;height:1px;background:var(--line)}
.copy{left:111px;top:3388px;font-size:11px;color:var(--muted)}
.legal{right:129px;top:3388px;font-size:11px;color:var(--muted);display:flex;gap:10px}
.legal span+span::before{content:"|";margin-right:10px;color:#55637f}
</style>
</head>
<body>

<!-- header -->
<div class="abs brand" style="left:89px;top:22px;font-size:30px"><span class="brand-dot"></span>Veltranoquest.ai</div>
<div class="btn btn-light" style="left:867px;top:19px;width:243px;height:46px">Talk to a Product Specialist</div>

<!-- hero -->
<h1 class="abs hero-title">BOOST YOUR<br>DRIVING <span class="accent">SCHOOL</span></h1>
<div class="abs hero-sub">with a 24/7 Voice Agent</div>
<div class="abs hero-tag">Automate Calls. Answer Questions Instantly. Never Miss a Student Again.</div>
<div class="btn btn-green" style="left:89px;top:410px;width:191px;height:49px">Book a Free Demo</div>
<div class="btn btn-outline" style="left:288px;top:410px;width:178px;height:49px">See It in Action</div>
<div class="abs" style="left:622px;top:148px;width:470px;height:300px;background:var(--panel);border-radius:4px"></div>
<div class="photo" role="img" aria-label="Laptop showing an AI vehicle dashboard over a glowing network backdrop" style="left:640px;top:165px;width:470px;height:317px;background:linear-gradient(135deg,#2d3a3e,#1b5b6a 45%,#0d3d46 70%,#162a30)"></div>

<!-- voice band 1 -->
<div class="voice-band" role="img" aria-label="Green audio waveform band with a tall burst on the left" style="top:540px;--cx:22%"></div>

<!-- why -->
<div class="abs" style="left:109px;top:842px;width:488px;height:316px;background:var(--panel);border-radius:4px"></div>
<div class="photo" role="img" aria-label="Student in a car back seat reviewing lessons on a tablet" style="left:91px;top:823px;width:488px;height:317px;background:linear-gradient(120deg,#3d5a32,#2a2f2c 45%,#1b1d21)"></div>
<h2 class="abs why-title">WHY DRIVING SCHOOLS<br><span class="accent">CHOOSE VOICE AGENTS</span></h2>
<p class="abs why-text">Running a driving school means juggling lesson schedules, student questions, staff changes, and constant phone calls. A Voice Agent is your AI-powered assistant that answers the phone 24/7, handles routine questions, and gives your staff room to breathe—without the cost of hiring more people.</p>

<!-- problems -->
<h2 class="section-title" style="top:1268px">KEY PROBLEMS <span class="accent">SOLVED</span></h2>
<div class="problem" style="left:119px">
  <svg viewBox="0 0 44 44" fill="none" stroke="#fff" stroke-width="1.8" stroke-linecap="round" stroke-linejoin="round"><path d="M10 6l6 7-3 4c2 5 6 9 11 11l4-3 7 6-4 5C19 35 8 24 6 10z"/><path d="M26 8a9 9 0 0 1 9 9M26 13a4 4 0 0 1 4 4" stroke="var(--green)"/></svg>
  <h3>CALL VOLUME &amp;<br>REPETITIVE QUESTIONS</h3>
  <p>Let your voice agent handle<br>calls about:</p>
  <ul><li>Pricing</li><li>Permit requirements</li><li>Class availability</li><li>Road test steps</li></ul>
  <p><b>Result:</b> Less time answering the same questions, more time delivering great lessons.</p>
</div>
<div class="problem" style="left:446px">
  <svg viewBox="0 0 44 44" fill="none" stroke="#fff" stroke-width="1.8" stroke-linecap="round" stroke-linejoin="round"><circle cx="22" cy="14" r="9" stroke="var(--green)"/><path d="M24 10h-3a2 2 0 0 0 0 4h2a2 2 0 0 1 0 4h-4M22 8v2M22 18v2" stroke="var(--green)"/><path d="M6 32l7-4h8a2 2 0 0 1 0 4h-5M6 38l5-2h12l12-8a2 2 0 0 0-3-3l-8 5"/></svg>
  <h3>NO EXPENSIVE TECH<br>INVESTMENT</h3>
  <p>Voice agents run in the cloud and integrate with your existing phone system.</p>
  <p class="result"><b>Result:</b> No hardware, low setup costs, and immediate ROI.</p>
</div>
<div class="problem" style="left:773px">
  <svg viewBox="0 0 44 44" fill="none" stroke="#fff" stroke-width="1.8" stroke-linecap="round"><circle cx="10" cy="10" r="4"/><circle cx="22" cy="8" r="4"/><circle cx="34" cy="10" r="4"/><path d="M4 24c0-5 3-7 6-7s6 2 6 7M16 20c0-5 3-6 6-6s6 1 6 6M28 24c0-5 3-7 6-7"/><circle cx="30" cy="32" r="8" stroke="var(--green)"/><path d="M26 32l3 3 5-5" stroke="var(--green)"/></svg>
  <h3>INSTRUCTOR ABSENCES<br>&amp; RESCHEDULING</h3>
  <p>Integrated with your booking system, your voice agent can help reschedule or notify students of changes.</p>
  <p class="result"><b>Result:</b> Fewer cancellations and smoother communication.</p>
</div>
<div class="abs dots"><span></span><span></span></div>

<!-- voice band 2 -->
<div class="voice-band" role="img" aria-label="Green audio waveform band with a tall burst on the right" style="top:1705px;--cx:83%"></div>

<!-- benefits -->
<h2 class="section-title" style="top:1960px">REAL BENEFITS FOR <span class="accent">YOUR SCHOOL</span></h2>
<div class="abs orbit"></div>
<div class="abs brand center-brand"><span class="brand-dot"></span>Veltranoquest.ai</div>

<div class="benefit-icon" style="left:424px;top:2099px"><svg viewBox="0 0 28 28" fill="none" stroke="#fff" stroke-width="1.6" stroke-linecap="round"><path d="M7 5l4 4-2 3c1 3 4 6 7 7l3-2 4 4-3 3C11 24 4 17 4 8z"/></svg></div>
<div class="benefit-icon" style="left:394px;top:2202px"><svg viewBox="0 0 28 28" fill="none" stroke="#fff" stroke-width="1.6" stroke-linecap="round"><circle cx="14" cy="15" r="9"/><path d="M14 10v5l3 2M12 3h4"/></svg></div>
<div class="benefit-icon" style="left:419px;top:2296px"><svg viewBox="0 0 28 28" fill="none" stroke="#fff" stroke-width="1.6" stroke-linecap="round"><circle cx="14" cy="9" r="4"/><path d="M6 24c0-5 4-8 8-8s8 3 8 8M4 12l3 2M24 12l-3 2"/></svg></div>
<div class="benefit-icon" style="left:732px;top:2099px"><svg viewBox="0 0 28 28" fill="none" stroke="#fff" stroke-width="1.6" stroke-linecap="round"><circle cx="14" cy="10" r="6"/><path d="M14 7v6M12 9h3M4 22l6-3h6l8-4"/></svg></div>
<div class="benefit-icon" style="left:762px;top:2202px"><svg viewBox="0 0 28 28" fill="none" stroke="#fff" stroke-width="1.6" stroke-linecap="round"><rect x="6" y="4" width="12" height="20" rx="2"/><path d="M9 12l2 2 4-4M20 10h4v12h-6"/></svg></div>
<div class="benefit-icon" style="left:737px;top:2296px"><svg viewBox="0 0 28 28" fill="none" stroke="#fff" stroke-width="1.6" stroke-linecap="round"><path d="M14 3l9 4v7c0 6-4 9-9 11-5-2-9-5-9-11V7z"/><path d="M10 14l3 3 5-6"/></svg></div>

<div class="benefit left" style="right:811px;top:2108px">24/7 Live Call Support<br>—No More Missed Calls</div>
<div class="benefit left" style="right:842px;top:2212px">Faster Response<br>Times = Happier Customers</div>
<div class="benefit left" style="right:815px;top:2308px">Less Admin Stress for<br>You and Your Team</div>
<div class="benefit" style="left:820px;top:2104px">Lower Operating Costs<br>Than Live Staff</div>
<div class="benefit" style="left:852px;top:2212px">More Bookings, Fewer No<br>-Shows</div>
<div class="benefit" style="left:826px;top:2316px">A Modern, Professional<br>Image</div>

<!-- testimonials -->
<h2 class="section-title" style="top:2510px">OUR <span class="accent">TESTIMONIALS</span></h2>
<div class="quote" style="left:131px"><div class="quote-mark">“</div><p>“Lorem Ipsum is simply dummy text of the printing and typesetting industry. Lorem Ipsum has been the industry's standard dummy text ever since the 1500s, when an unknown printer took a galley of type and scrambled.”</p><div class="author">Maren Oduya</div></div>
<div class="quote" style="left:373px"><div class="quote-mark">“</div><p>“Lorem Ipsum is simply dummy text of the printing and typesetting industry. Lorem Ipsum has been the industry's standard dummy text ever since the 1500s, when an unknown printer took a galley of type and scrambled.”</p><div class="author">Lio Brankett</div></div>
<div class="quote" style="left:612px"><div class="quote-mark">“</div><p>“Lorem Ipsum is simply dummy text of the printing and typesetting industry. Lorem Ipsum has been the industry's standard dummy text ever since the 1500s, when an unknown printer took a galley of type and scrambled.”</p><div class="author">DELA Voss</div></div>
<div class="quote" style="left:849px"><div class="quote-mark">“</div><p>“Lorem Ipsum is simply dummy text of the printing and typesetting industry. Lorem Ipsum has been the industry's standard dummy text ever since the 1500s, when an unknown printer took a galley of type and scrambled.”</p><div class="author">Jessa Ruml</div></div>

<!-- cta -->
<div class="abs cta"></div>
<div class="abs cta-art" role="img" aria-label="Glowing wireframe paper plane made of connected points"></div>
<h2 class="abs cta-title">READY TO AUTOMATE <span class="accent">YOUR<br>FRONT DESK?</span></h2>
<p class="abs cta-text">Let your school sound smarter, faster, and more helpful—24 hours a day.</p>
<div class="btn btn-outline" style="left:524px;top:3103px;width:159px;height:47px">Book a Free Demo</div>
<div class="btn btn-green" style="left:693px;top:3103px;width:218px;height:47px">Talk to a Product Specialist</div>
<div class="btn btn-outline" style="left:920px;top:3103px;width:129px;height:47px">See It in Action</div>

<!-- footer -->
<div class="abs brand footer-brand"><span class="brand-dot"></span>Veltranoquest.ai</div>
<div class="social on" style="left:910px"></div>
<div class="social" style="left:954px"></div>
<div class="social" style="left:996px"></div>
<div class="social" style="left:1035px"></div>
<div class="abs footer-rule"></div>
<div class="abs copy">© 2025. All rights reserved.</div>
<div class="abs legal"><span>Terms of Service</span><span>Privacy and Cookies</span></div>

</body>
</html>
```